2 banners on the outside wall of the hall

Banner 1:
Kalvamo specializes in the planning, construction, and maintenance of high-quality pond systems, particularly swimming ponds, natural pools, garden ponds, koi ponds, streams, and waterfalls. Learn more at www.kalvamo.de
The following data should be included:
Planning and construction of swimming ponds and natural pools, as well as garden ponds and koi ponds
100% organic
Individually planned
Over 20 years of experience
04271 6632907
www.kalvamo.de
“Logo-Kalvamo”
Banner 2:
Lumo-Grün is the online shop for high-quality aquatic plants for ponds and aquariums.
More information at https://lumo-gruen.de
Online shop for pond plants and water lilies, as well as aquarium plants and accessories
Over 400 plant species
Top gardener quality
Secure packaging & fast shipping
04271 6632906
www.lumo-gruen. de
“Logo Lumo green”
Here's roughly what we envision:
The designs for each banner should be clearly visible and include everything needed, without appearing cluttered. In other words, it should be immediately clear what the banner is about.
We should also be made aware of our unique selling points and advantages.
It is important that the banners also harmonize visually with each other.
We liked the banner image in the attachment and it serves as inspiration.
The banner print data is produced as follows:
• Banner size: Width x Height: 3880 mm x 1880 mm
• Material: Mesh banner, PVFormat: PDF (X-3:2000)
• Fonts: converted into paths
• Trim allowance: +2 mm all around
• Color space: CMYK
• Resolution: 72 dpi (recommended) at 1:1 resolution
Look and feel
Each slider illustrates characteristics of the customer's brand and the style your logo design should communicate.

```html
<!DOCTYPE html>
<html lang="de">
<head>
<meta charset="utf-8">
<title>Kalvamo &amp; Lumo-Grün – Banner</title>
<link href="https://fonts.googleapis.com/css2?family=Montserrat:wght@500;700;800;900&display=swap" rel="stylesheet">
<style>
  :root {
    --green-dark: #0b4f26;
    --green-mid: #157a37;
    --green-light: #3cb64a;
    --blue-dark: #0f7fc4;
    --blue-mid: #2196d3;
    --blue-light: #5fcbdc;
    --yellow: #fdd323;
    --grey-label: #e6e4e4;
    --white: #ffffff;
    --ink: #111111;
    --tick: #7ac043;
    --gap: #ffffff;
  }
  * { box-sizing: border-box; margin: 0; padding: 0; }
  html, body { width: 1200px; height: 1200px; overflow: hidden; background: var(--gap); }
  body { font-family: "Montserrat", sans-serif; position: relative; }

  .banner { position: absolute; left: 0; width: 1200px; height: 581px; overflow: hidden; }
  .banner--pond { top: 0; }
  .banner--plants { top: 619px; }

  .brand-panel { position: absolute; left: 0; top: 0; width: 426px; height: 581px; }
  .banner--pond .brand-panel { background: radial-gradient(ellipse 70% 60% at 50% 50%, var(--green-light), var(--green-mid) 60%, var(--green-dark)); }
  .banner--plants .brand-panel { background: radial-gradient(ellipse 70% 60% at 45% 55%, var(--blue-light), var(--blue-mid) 60%, var(--blue-dark)); }

  .headline-band { position: absolute; left: 426px; top: 0; width: 774px; height: 107px;
    display: flex; align-items: center; justify-content: center; text-align: center; }
  .banner--pond .headline-band { background: linear-gradient(90deg, var(--green-dark), var(--green-mid)); }
  .banner--plants .headline-band { background: linear-gradient(90deg, var(--blue-mid), var(--blue-dark)); }
  .headline { color: var(--white); font-weight: 900; font-size: 26px; line-height: 28px; letter-spacing: .3px; padding-left: 50px; }

  .scene { position: absolute; left: 422px; top: 107px; width: 778px; height: 474px; }
  .scene--garden-pond { background:
      radial-gradient(ellipse 40% 30% at 80% 25%, #6d6fc8 0%, transparent 70%),
      radial-gradient(ellipse 60% 50% at 40% 55%, #4f7a45, transparent 75%),
      linear-gradient(180deg, #2f5a22 0%, #557a3a 35%, #6f7f54 70%, #8a8a6a 100%); }

  .brand-name { position: absolute; color: var(--white); font-weight: 800; display: flex; align-items: center; gap: 14px; }
  .brand-name .brand-dot { width: 22px; height: 22px; border-radius: 50%; background: var(--yellow); }
  .banner--pond .brand-name { left: 52px; top: 50px; font-size: 58px; }
  .banner--plants .brand-name { left: 40px; top: 670px; font-size: 54px; }
  .banner--plants .brand-name { top: 50px; }

  .feature { position: absolute; left: 29px; display: flex; align-items: center; }
  .feature-box { width: 86px; height: 69px; display: flex; align-items: center; justify-content: center; box-shadow: 0 1px 3px rgba(0,0,0,.25); position: relative; z-index: 1; }
  .feature-box--wide { width: 95px; }
  .feature-box--white { background: var(--white); }
  .feature-box--yellow { background: var(--yellow); }
  .feature-box svg { width: 46px; height: 46px; }
  .feature-label { height: 54px; display: flex; align-items: center; padding: 0 12px 0 11px; font-weight: 800; font-size: 17px; color: var(--ink); margin-left: -1px; }
  .feature-label--yellow { background: var(--yellow); }
  .feature-label--grey { background: var(--grey-label); }
  .feature-label--white { background: var(--white); }
  .feature-label--tall { line-height: 22px; }

  .contact { position: absolute; left: 35px; display: flex; align-items: center; gap: 13px; color: var(--white); font-weight: 900; font-size: 22px; }
  .contact-icon { width: 30px; height: 30px; border-radius: 50%; background: var(--white); display: flex; align-items: center; justify-content: center; }
  .contact-icon svg { width: 18px; height: 18px; }

  .scene-split { position: absolute; left: 422px; top: 106px; width: 778px; height: 475px; }
</style>
</head>
<body>

<section class="banner banner--pond">
  <div class="brand-panel">
    <div class="brand-name">Kalvamo</div>

    <div class="feature" style="top:174px">
      <div class="feature-box feature-box--white"><svg viewBox="0 0 48 48"><rect x="4" y="10" width="32" height="32" rx="6" fill="none" stroke="var(--tick)" stroke-width="4"/><path d="M12 25 L20 33 L42 6" fill="none" stroke="var(--tick)" stroke-width="6" stroke-linecap="round" stroke-linejoin="round"/></svg></div>
      <div class="feature-label feature-label--yellow">100% biologisch</div>
    </div>
    <div class="feature" style="top:264px">
      <div class="feature-box feature-box--yellow"><svg viewBox="0 0 48 48"><rect x="4" y="10" width="32" height="32" rx="6" fill="none" stroke="var(--white)" stroke-width="4"/><path d="M12 25 L20 33 L42 6" fill="none" stroke="var(--white)" stroke-width="6" stroke-linecap="round" stroke-linejoin="round"/></svg></div>
      <div class="feature-label feature-label--grey">Individuell geplant</div>
    </div>
    <div class="feature" style="top:355px">
      <div class="feature-box feature-box--white feature-box--wide"><svg viewBox="0 0 48 48"><rect x="4" y="10" width="32" height="32" rx="6" fill="none" stroke="var(--tick)" stroke-width="4"/><path d="M12 25 L20 33 L42 6" fill="none" stroke="var(--tick)" stroke-width="6" stroke-linecap="round" stroke-linejoin="round"/></svg></div>
      <div class="feature-label feature-label--yellow" style="width:258px">Über 20 Jahre Erfahrung</div>
    </div>

    <div class="contact" style="top:492px">
      <span class="contact-icon"><svg viewBox="0 0 24 24"><path d="M6 3 L9 3 L10 8 L8 9.5 C9 12 11.5 14.5 14 15.5 L15.5 13.5 L20.5 14.5 L20.5 18 C20.5 19.5 19 20.5 17.5 20.5 C10 20 4 14 3.5 6.5 C3.5 4.5 4.5 3 6 3 Z" fill="var(--tick)"/></svg></span>
      04271 6632907
    </div>
    <div class="contact" style="top:532px">
      <span class="contact-icon"><svg viewBox="0 0 24 24"><circle cx="12" cy="12" r="9" fill="var(--tick)"/><path d="M3 12 H21 M12 3 V21 M12 3 C7 8 7 16 12 21 M12 3 C17 8 17 16 12 21 M5 7.5 H19 M5 16.5 H19" stroke="var(--white)" stroke-width="1.2" fill="none"/></svg></span>
      www.kalvamo.de
    </div>
  </div>

  <div class="headline-band">
    <h2 class="headline">Planung und Bau von<br>Schwimmteichen und Naturpools<br>sowie Gartenteichen und Koiteichen</h2>
  </div>

  <div class="scene scene--garden-pond" role="img" aria-label="Foto: naturnaher Schwimmteich mit Holzsteg, Liegen, Wasserfall, blühender Uferbepflanzung und Kois im klaren Wasser"></div>
</section>

<section class="banner banner--plants">
  <div class="brand-panel">
    <div class="brand-name"><span class="brand-dot"></span>Lumo-Grün</div>

    <div class="feature" style="top:174px">
      <div class="feature-box feature-box--white"><svg viewBox="0 0 48 48"><rect x="4" y="10" width="32" height="32" rx="6" fill="none" stroke="var(--tick)" stroke-width="4"/><path d="M12 25 L20 33 L42 6" fill="none" stroke="var(--tick)" stroke-width="6" stroke-linecap="round" stroke-linejoin="round"/></svg></div>
      <div class="feature-label feature-label--yellow" style="width:266px">Über 400 Pflanzenarten</div>
    </div>
    <div class="feature" style="top:264px">
      <div class="feature-box feature-box--yellow"><svg viewBox="0 0 48 48"><rect x="4" y="10" width="32" height="32" rx="6" fill="none" stroke="var(--white)" stroke-width="4"/><path d="M12 25 L20 33 L42 6" fill="none" stroke="var(--white)" stroke-width="6" stroke-linecap="round" stroke-linejoin="round"/></svg></div>
      <div class="feature-label feature-label--white" style="width:233px">TOP-Gärtner-Qualität</div>
    </div>
    <div class="feature" style="top:355px">
      <div class="feature-box feature-box--white feature-box--wide"><svg viewBox="0 0 48 48"><rect x="4" y="10" width="32" height="32" rx="6" fill="none" stroke="var(--tick)" stroke-width="4"/><path d="M12 25 L20 33 L42 6" fill="none" stroke="var(--tick)" stroke-width="6" stroke-linecap="round" stroke-linejoin="round"/></svg></div>
      <div class="feature-label feature-label--yellow feature-label--tall" style="width:258px">Sichere Verpackung &amp;<br>Schneller Versand</div>
    </div>

    <div class="contact" style="top:493px">
      <span class="contact-icon"><svg viewBox="0 0 24 24"><path d="M6 3 L9 3 L10 8 L8 9.5 C9 12 11.5 14.5 14 15.5 L15.5 13.5 L20.5 14.5 L20.5 18 C20.5 19.5 19 20.5 17.5 20.5 C10 20 4 14 3.5 6.5 C3.5 4.5 4.5 3 6 3 Z" fill="var(--tick)"/></svg></span>
      04271 6632906
    </div>
    <div class="contact" style="top:531px">
      <span class="contact-icon"><svg viewBox="0 0 24 24"><circle cx="12" cy="12" r="9" fill="var(--tick)"/><path d="M3 12 H21 M12 3 V21 M12 3 C7 8 7 16 12 21 M12 3 C17 8 17 16 12 21 M5 7.5 H19 M5 16.5 H19" stroke="var(--white)" stroke-width="1.2" fill="none"/></svg></span>
      www.lumo-gruen.de
    </div>
  </div>

  <div class="headline-band">
    <h2 class="headline">Online-Shop für<br>Teichpflanzen und Seerosen,<br>sowie Aquarienpflanzen und Zubehör</h2>
  </div>

  <svg class="scene-split" viewBox="0 0 778 475" preserveAspectRatio="none">
    <defs>
      <linearGradient id="pond-water" x1="0" y1="0" x2="0" y2="1">
        <stop offset="0" stop-color="#4c6a3c"/>
        <stop offset=".5" stop-color="#6f8f48"/>
        <stop offset="1" stop-color="#5a7a3e"/>
      </linearGradient>
      <linearGradient id="aquarium-water" x1="0" y1="0" x2="1" y2="1">
        <stop offset="0" stop-color="#2f6a34"/>
        <stop offset=".5" stop-color="#4a7a2e"/>
        <stop offset="1" stop-color="#3b5a24"/>
      </linearGradient>
    </defs>
    <g role="img" aria-label="Foto: Gartenteich mit Seerosen, Schwimmblättern und Iris">
      <path d="M0 0 H405 C450 60 440 150 390 230 C340 310 345 400 380 475 H0 Z" fill="url(#pond-water)"/>
    </g>
    <g role="img" aria-label="Foto: bepflanztes Aquarium mit roten und grünen Wasserpflanzen, Wurzelholz und kleinen Fischen">
      <path d="M405 0 H778 V475 H380 C345 400 340 310 390 230 C440 150 450 60 405 0 Z" fill="url(#aquarium-water)"/>
    </g>
    <path d="M405 0 C450 60 440 150 390 230 C340 310 345 400 380 475" fill="none" stroke="var(--white)" stroke-width="4"/>
  </svg>
</section>

</body>
</html>
```